Marketing Company with a Passion
Khalid R Al-Sudairi
Project: Marketing Company with a Passion
Marketing Company with a Passion - Marketing
Creative Brief
Professional
General Manager
Saudi : Level 3 East Wing Gate B, Fanar Court Tahlia Street P.O.BOX 51764, 11532 Riyadh Riyadh, Kingdom of Saudi Arabia England: Level 12 Penwick Tower 41 Fenmore Lane London EC3N 2RT
Saudi : + 966 1 572 9146 --- England : +44 (0)207 814 3062
khalid.r@velquora.com
velquora.com
i will be needing two versions of the business card one for Saudi and one for England all should be the same design but the address and office numbers should be different, website and email are the same also the Mobile number should be the same
please be very creative in your design, id like it to be simple yet attractive, please add a space for my Skype contact which is : khalid.alsudairi id also like a blank one to add more employees contacts on them during hiring. or in the event of us changing offices main things on the business card should be : 1. Name, landline, Mobile, address, email, Skype and lastly company website on one face id like the companies name and contact details, on the other side just the logo with some artwork that would match it, the style is Arabiesc Important note ( Cards will be Translated into Arabic for the Saudi market by a local designer. so id also like a blank copy of the design to add info in arabic ) Regarding Stationaries. same design as the business card with same tone, contact details to the office in 2 versions, Saudi and England ( Address, landline and website only ) id also like a blank one to be translated into arabic as well. Thank you and Good luck
Concepts
khalidalsudairi khalidalsudairi
i would like the logo to be placed on the back, and only the Logo with some artistic design
*** PLEASE BE ADVISED, ONE CARD FOR SAUDI, ONE CARD FOR ENGLAND ***** REFER TO BREF FOR DETAIL
forgot to mention in the brief, id also like a billing form thank you
Dear all welcome. I'm expecting some very attractive work from you guys, these cards and stationaries will be presented to some of the worlds biggest companies and governments so make it count. the winner will be handed more work from my other projects so this is not a one time thing All file formats are in .ia

```html
<!DOCTYPE html>
<html lang="en">
<head>
<meta charset="utf-8">
<title>Velquora Stationery Concept</title>
<link href="https://fonts.googleapis.com/css2?family=Cinzel:wght@400;600&family=Lato:wght@400;700&display=swap" rel="stylesheet">
<style>
  :root {
    --bg-dark: #5a5a5a;
    --bg-light: #b4b4b4;
    --gold: #b8975a;
    --gold-light: #dcc38b;
    --gold-dark: #7a6033;
    --black: #111111;
    --paper: #fbfaf7;
    --ink: #4a4a4a;
    --label: #2e2e2e;
  }
  * { margin: 0; padding: 0; box-sizing: border-box; }
  html, body { width: 1200px; height: 274px; overflow: hidden; }
  body {
    position: relative;
    background: linear-gradient(180deg, var(--bg-dark) 0%, var(--bg-light) 100%);
    font-family: "Lato", sans-serif;
    color: var(--ink);
  }
  .item { position: absolute; box-shadow: 0 2px 5px rgba(0,0,0,.35); }
  .gold-fill { background: linear-gradient(135deg, var(--gold-dark), var(--gold-light) 50%, var(--gold)); }
  .brand { font-family: "Cinzel", serif; font-weight: 600; color: var(--gold); letter-spacing: .12em; white-space: nowrap; }
  .mark { border-radius: 50%; background: radial-gradient(circle, var(--gold-light), var(--gold-dark)); }
  .label { position: absolute; left: 0; width: 100%; bottom: -9px; font-size: 4px; color: var(--label); text-align: center; white-space: nowrap; }

  .header { position: absolute; left: 40px; top: 14px; width: 110px; text-align: center; }
  .header .mark { width: 30px; height: 30px; margin: 0 auto 4px; }
  .header .brand { font-size: 8px; }
  .header .sub { font-size: 5px; color: #e4e4e4; margin-top: 3px; }

  .card { width: 88px; height: 54px; padding: 7px 8px; font-size: 3.4px; line-height: 1.45; overflow: hidden; }
  .card .name { font-weight: 700; font-size: 4.6px; margin-bottom: 2px; }
  .card-front { left: 12px; top: 126px; background: var(--paper); }
  .card-front .name { color: var(--gold-dark); }
  .card-front .band { position: absolute; left: 0; right: 0; bottom: 0; height: 5px; }
  .card-front .corner { position: absolute; right: 7px; top: 7px; width: 12px; height: 12px; }
  .card-back-gold { left: 108px; top: 126px; display: flex; align-items: center; justify-content: center; }
  .card-back-gold .brand { color: var(--black); font-size: 6px; }
  .card-back-black { left: 12px; top: 190px; background: var(--black); display: flex; flex-direction: column; align-items: center; justify-content: center; }
  .card-back-black .mark { width: 22px; height: 22px; }
  .card-back-black .brand { font-size: 5px; margin-top: 3px; }
  .card-alt { left: 108px; top: 190px; background: var(--black); color: #d8d8d8; }
  .card-alt .name { color: var(--gold-light); }
  .card-alt .band { position: absolute; right: 0; top: 0; bottom: 0; width: 5px; }

  .letterhead { left: 234px; top: 28px; width: 122px; height: 228px; background: var(--paper); padding: 30px 10px 10px 16px; font-size: 3px; line-height: 1.55; }
  .letterhead .edge { position: absolute; right: 0; top: 0; bottom: 0; width: 5px; }
  .letterhead .mark { position: absolute; left: 56px; top: 8px; width: 11px; height: 11px; }
  .letterhead p { margin-bottom: 4px; }
  .letterhead .sign { font-family: "Cinzel", serif; font-size: 5px; color: var(--gold-dark); margin: 8px 0 2px; }
  .letterhead .foot { position: absolute; left: 16px; right: 10px; bottom: 8px; font-size: 2.4px; line-height: 1.4; color: var(--gold-dark); }

  .slip { left: 444px; top: 34px; width: 180px; height: 56px; background: var(--paper); }
  .slip .mark { position: absolute; left: 84px; top: 8px; width: 12px; height: 12px; }
  .slip .edge { position: absolute; left: 0; right: 0; bottom: 0; height: 5px; }

  .envelope { left: 444px; top: 140px; width: 186px; height: 76px; background: var(--paper); }
  .envelope .flap { position: absolute; left: 0; right: 0; top: 0; height: 16px; }
  .envelope .addr { position: absolute; left: 10px; bottom: 9px; font-size: 3px; line-height: 1.5; }

  .folder-gold { left: 660px; top: 34px; width: 168px; height: 216px; }
  .folder-black { left: 828px; top: 34px; width: 162px; height: 182px; background: var(--black); display: flex; flex-direction: column; align-items: center; justify-content: center; }
  .folder-black .mark { width: 66px; height: 66px; }
  .folder-black .brand { font-size: 9px; margin-top: 10px; }
  .pocket { left: 828px; top: 212px; width: 162px; height: 38px; }
  .pocket-card { left: 822px; top: 202px; width: 36px; height: 36px; background: var(--black); display: flex; align-items: center; justify-content: center; }
  .pocket-card .mark { width: 18px; height: 18px; }
  .folder-label { position: absolute; left: 660px; top: 254px; width: 330px; font-size: 4px; color: var(--label); text-align: center; }

  .cd { left: 1022px; top: 12px; width: 144px; height: 144px; border-radius: 50%; background: var(--paper); }
  .cd .ring { position: absolute; left: 22px; top: 22px; width: 100px; height: 100px; border-radius: 50%; border: 1px solid var(--gold-light); }
  .cd .hole { position: absolute; left: 60px; top: 60px; width: 24px; height: 24px; border-radius: 50%; background: #bdbdbd; border: 4px solid #e6e6e6; }

  .cd-sleeve { left: 1000px; top: 170px; width: 160px; height: 88px; display: flex; align-items: center; padding-left: 24px; }
  .cd-sleeve .mark { width: 38px; height: 38px; background: var(--black); }
</style>
</head>
<body>
  <header class="header">
    <div class="mark"></div>
    <div class="brand">VELQUORA</div>
    <div class="sub">Stationery Concept</div>
  </header>

  <section class="item card card-front">
    <div class="corner mark"></div>
    <div class="name">Khalid R Al-Sudairi</div>
    <div>General Manager</div>
    <div>T: + 966 1 572 9146</div>
    <div>E: khalid.r@velquora.com</div>
    <div>Skype: khalid.alsudairi</div>
    <div>velquora.com</div>
    <div class="band gold-fill"></div>
  </section>
  <section class="item card card-back-gold gold-fill"><span class="brand">VELQUORA</span></section>
  <section class="item card card-back-black"><div class="mark"></div><div class="brand">VELQUORA</div></section>
  <section class="item card card-alt">
    <div class="name">Khalid R Al-Sudairi</div>
    <div>General Manager</div>
    <div>T: +44 (0)207 814 3062</div>
    <div>E: khalid.r@velquora.com</div>
    <div>velquora.com</div>
    <div class="band gold-fill"></div>
  </section>

  <section class="item letterhead">
    <div class="edge gold-fill"></div>
    <div class="mark"></div>
    <p><b>Dear Client</b></p>
    <p>Thank you for your continued trust in our team. We look forward to building lasting campaigns together with passion and care.</p>
    <p>Please find enclosed the proposal for your review.</p>
    <p>Sincerely,</p>
    <div class="sign">K. Al-Sudairi</div>
    <p>Khalid R Al-Sudairi<br>General Manager</p>
    <div class="foot">Level 3 East Wing Gate B, Fanar Court Tahlia Street P.O.BOX 51764, 11532 Riyadh<br>+ 966 1 572 9146 · velquora.com</div>
    <span class="label">Letterhead</span>
  </section>

  <section class="item slip"><div class="mark"></div><div class="edge gold-fill"></div><span class="label">Compliment Slip</span></section>
  <section class="item envelope">
    <div class="flap gold-fill"></div>
    <div class="addr">Level 12 Penwick Tower 41 Fenmore Lane<br>London EC3N 2RT</div>
    <span class="label">Envelope</span>
  </section>

  <section class="item folder-gold gold-fill"></section>
  <section class="item folder-black"><div class="mark"></div><div class="brand">VELQUORA</div></section>
  <section class="item pocket gold-fill"></section>
  <section class="item pocket-card"><div class="mark"></div></section>
  <div class="folder-label">Folder</div>

  <section class="item cd"><div class="ring"></div><div class="hole"></div><span class="label" style="bottom:-10px">CD Label</span></section>
  <section class="item cd-sleeve gold-fill"><div class="mark"></div></section>
</body>
</html>
```